Algae Cream Package Concept

Creative Brief — Solvane: Phytoplankton Rescue Cream (100 ml)
Product Snapshot
Name: Solvane: Phytoplankton Rescue Cream
Format: 100 ml / 3.4 fl oz tube or airless pump (dieline provided)
Dieline attached:
Purpose & Key Benefits
Rescue dry or damaged skin—especially eczema & psoriasis.
All‑over use: hands, feet, elbows, knees, face, body.
Repairs barrier · Deep hydration · Calms irritation · Antioxidant shield.
Usage
Longevity: ~30 days when used daily on 10 in² of skin.
How: Apply pea‑size to clean, damp skin; massage ≥1 min; reapply as needed.
Ingredients
Label Ingredients:
Aloe Barbadensis (Aloe) Leaf Juice, Butyrospermum Parkii (Shea) Butter, Aqua (and) Propanediol (and) Nannochloropsis Gaditana (Phytoplankton) Extract, Simmondsia Chinensis (Jojoba) Seed Oil, Sodium Lactate, Cetyl Alcohol, Cetearyl Olivate (and) Sorbitan Olivate (Tersal 400), Panthenol (Vitamin B5), Gluconolactone (and) Sodium
Benzoate (and) Calcium Gluconate (Marquil Prime), Illite (French Green Clay).
Look & Feel (for designer)
Minimal, ocean‑inspired, premium yet approachable. Off‑white base, deep‑teal accent, subtle algae texture.
Must‑Haves on Pack
Product name + “Rescue Cream” descriptor
Net weight (100 ml / 3.4 fl oz)
Tagline: “Reunite your skin with Earth’s base nutrition.”
Copy snippet: “Powered by sustainably grown phytoplankton.”
Icons: Vegan • Cruelty‑Free • Reef‑Safe • Recyclable
www.tolvenrise.com

```html
<!DOCTYPE html>
<html lang="en">
<head>
<meta charset="utf-8">
<title>Solvane Phytoplankton Rescue Cream</title>
<link href="https://fonts.googleapis.com/css2?family=Montserrat:wght@600;700;800&display=swap" rel="stylesheet">
<style>
  :root {
    --backdrop: #ececec;
    --label: #ffffff;
    --teal: #2f5e61;
    --teal-soft: #dfe8e8;
  }
  * { margin: 0; padding: 0; box-sizing: border-box; }
  html, body { width: 1200px; height: 750px; overflow: hidden; }
  body {
    background: var(--backdrop);
    font-family: "Montserrat", sans-serif;
    color: var(--teal);
    display: flex;
    align-items: center;
    justify-content: center;
    gap: 90px;
  }
  .label {
    width: 280px;
    height: 640px;
    background: var(--label);
    border-radius: 6px;
    display: flex;
    flex-direction: column;
    align-items: center;
    overflow: hidden;
  }
  .algae-texture {
    width: 100%;
    height: 140px;
    flex-shrink: 0;
    background: linear-gradient(180deg, var(--label) 0%, var(--teal-soft) 50%, var(--label) 100%);
  }
  .band-thin { width: 100%; height: 4px; background: var(--teal); flex-shrink: 0; }
  .band-thick { width: 100%; height: 9px; background: var(--teal); flex-shrink: 0; }
  .label--tube .band-thick { margin-top: 8px; }
  .label--pump .band-thin { margin-bottom: 8px; }
  .copy {
    flex: 1;
    width: 100%;
    display: flex;
    flex-direction: column;
    align-items: center;
    text-align: center;
    padding: 26px 18px 16px;
  }
  .brand {
    font-weight: 800;
    font-size: 40px;
    line-height: 1;
    letter-spacing: 0.5px;
  }
  .product {
    font-weight: 700;
    font-size: 18px;
    letter-spacing: 0.5px;
    margin-top: 2px;
    padding-bottom: 8px;
    border-bottom: 2px solid var(--teal);
  }
  .tagline {
    font-weight: 700;
    font-size: 11.5px;
    line-height: 1.15;
    margin-top: 10px;
  }
  .descriptor {
    margin-top: 18px;
    background: var(--teal);
    color: var(--label);
    font-weight: 800;
    font-size: 13px;
    letter-spacing: 6px;
    padding: 5px 12px 5px 18px;
  }
  .benefit {
    font-weight: 700;
    font-size: 11px;
    line-height: 1.2;
    margin-top: 18px;
  }
  .divider { width: 26px; height: 2px; background: var(--teal); margin: 7px auto; }
  .snippet {
    font-weight: 600;
    font-size: 9.5px;
    line-height: 1.25;
    margin-top: 14px;
  }
  .claims {
    list-style: none;
    display: flex;
    gap: 10px;
    margin-top: 10px;
  }
  .claim {
    display: flex;
    flex-direction: column;
    align-items: center;
    gap: 3px;
    font-weight: 700;
    font-size: 6.5px;
    letter-spacing: 0.3px;
    width: 50px;
  }
  .claim svg { width: 20px; height: 20px; }
  .website {
    font-weight: 700;
    font-size: 8.5px;
    letter-spacing: 0.5px;
    margin-top: 10px;
  }
  .volume {
    margin-top: auto;
    font-weight: 800;
    font-size: 8.5px;
    display: flex;
    align-items: center;
    gap: 10px;
  }
  .volume .rule { width: 2px; height: 16px; background: var(--teal); }
</style>
</head>
<body>
  <section class="label label--tube">
    <div class="algae-texture" role="img" aria-label="Line pattern of flowing algae leaves in deep teal"></div>
    <div class="band-thin"></div>
    <div class="band-thick"></div>
    <div class="copy">
      <h1 class="brand">SOLVANE</h1>
      <p class="product">PHYTOPLANKTON</p>
      <p class="tagline">REUNITE YOUR SKIN WITH<br>EARTH’S BASE NUTRITION</p>
      <p class="descriptor">RESCUE CREAM</p>
      <div class="benefit">
        <p>RESCUE DRY<br>OR DAMAGED SKIN</p>
        <div class="divider"></div>
        <p>ESPECIALLY<br>ECZEMA &amp; PSORIASIS.</p>
      </div>
      <p class="snippet">Powered by sustainably<br>grown phytoplankton.</p>
      <ul class="claims">
        <li class="claim"><svg viewBox="0 0 20 20" aria-hidden="true"><circle cx="10" cy="10" r="8.5" fill="none" stroke="currentColor" stroke-width="1.5"/><path d="M6 10.5l2.7 2.7L14.2 7.5" fill="none" stroke="currentColor" stroke-width="1.6" stroke-linecap="round" stroke-linejoin="round"/></svg>VEGAN</li>
        <li class="claim"><svg viewBox="0 0 20 20" aria-hidden="true"><circle cx="10" cy="10" r="8.5" fill="none" stroke="currentColor" stroke-width="1.5"/><path d="M6 10.5l2.7 2.7L14.2 7.5" fill="none" stroke="currentColor" stroke-width="1.6" stroke-linecap="round" stroke-linejoin="round"/></svg>CRUELTY‑FREE</li>
        <li class="claim"><svg viewBox="0 0 20 20" aria-hidden="true"><circle cx="10" cy="10" r="8.5" fill="none" stroke="currentColor" stroke-width="1.5"/><path d="M6 10.5l2.7 2.7L14.2 7.5" fill="none" stroke="currentColor" stroke-width="1.6" stroke-linecap="round" stroke-linejoin="round"/></svg>REEF‑SAFE</li>
        <li class="claim"><svg viewBox="0 0 20 20" aria-hidden="true"><circle cx="10" cy="10" r="8.5" fill="none" stroke="currentColor" stroke-width="1.5"/><path d="M6 10.5l2.7 2.7L14.2 7.5" fill="none" stroke="currentColor" stroke-width="1.6" stroke-linecap="round" stroke-linejoin="round"/></svg>RECYCLABLE</li>
      </ul>
      <p class="website">www.tolvenrise.com</p>
      <p class="volume"><span>100ML</span><span class="rule"></span><span>3.4FLOZ</span></p>
    </div>
  </section>

  <section class="label label--pump">
    <div class="copy">
      <h1 class="brand">SOLVANE</h1>
      <p class="product">PHYTOPLANKTON</p>
      <p class="tagline">REUNITE YOUR SKIN WITH<br>EARTH’S BASE NUTRITION</p>
      <p class="descriptor">RESCUE CREAM</p>
      <div class="benefit">
        <p>RESCUE DRY<br>OR DAMAGED SKIN</p>
        <div class="divider"></div>
        <p>ESPECIALLY<br>ECZEMA &amp; PSORIASIS.</p>
      </div>
      <p class="snippet">Powered by sustainably<br>grown phytoplankton.</p>
      <ul class="claims">
        <li class="claim"><svg viewBox="0 0 20 20" aria-hidden="true"><circle cx="10" cy="10" r="8.5" fill="none" stroke="currentColor" stroke-width="1.5"/><path d="M6 10.5l2.7 2.7L14.2 7.5" fill="none" stroke="currentColor" stroke-width="1.6" stroke-linecap="round" stroke-linejoin="round"/></svg>VEGAN</li>
        <li class="claim"><svg viewBox="0 0 20 20" aria-hidden="true"><circle cx="10" cy="10" r="8.5" fill="none" stroke="currentColor" stroke-width="1.5"/><path d="M6 10.5l2.7 2.7L14.2 7.5" fill="none" stroke="currentColor" stroke-width="1.6" stroke-linecap="round" stroke-linejoin="round"/></svg>CRUELTY‑FREE</li>
        <li class="claim"><svg viewBox="0 0 20 20" aria-hidden="true"><circle cx="10" cy="10" r="8.5" fill="none" stroke="currentColor" stroke-width="1.5"/><path d="M6 10.5l2.7 2.7L14.2 7.5" fill="none" stroke="currentColor" stroke-width="1.6" stroke-linecap="round" stroke-linejoin="round"/></svg>REEF‑SAFE</li>
        <li class="claim"><svg viewBox="0 0 20 20" aria-hidden="true"><circle cx="10" cy="10" r="8.5" fill="none" stroke="currentColor" stroke-width="1.5"/><path d="M6 10.5l2.7 2.7L14.2 7.5" fill="none" stroke="currentColor" stroke-width="1.6" stroke-linecap="round" stroke-linejoin="round"/></svg>RECYCLABLE</li>
      </ul>
      <p class="website">www.tolvenrise.com</p>
      <p class="volume"><span>100ML</span><span class="rule"></span><span>3.4FLOZ</span></p>
    </div>
    <div class="band-thin"></div>
    <div class="band-thick"></div>
    <div class="algae-texture" role="img" aria-label="Line pattern of flowing algae leaves in deep teal"></div>
  </section>
</body>
</html>
```